Book cover for book about ex-wifes

I need a book cover for my new book called "Tidligere brude fra Solen, Stormen og Lindevang" - In english: "Former brides from Sun, Storm and Lindevang" (Hørsholm is a posh city in Denmark).

The book is by men for men about ex-wifes and about how to avoid getting them.
Is it a book from a sexologist and couples therapist to men on how to improve relations.

Men (and curious women)

• Something that indicate three types of ex-wifes

And the author name “Jonas Beltoft”
• Something that says something about relationships, couples and how to stay together (or how to avoid not breaking up)
• No hate

```html
<!DOCTYPE html>
<html lang="da">
<head>
<meta charset="utf-8">
<title>Tidligere brude fra Solen, Stormen og Lindevang – Jonas Beltoft</title>
<link rel="stylesheet" href="https://fonts.googleapis.com/css2?family=Anton&family=Oswald:wght@200;300;600;700&display=swap">
<style>
  :root {
    --page-bg: #ffffff;
    --title-red: #8e0606;
    --text-white: #ffffff;
    --paper-edge: #e9e2d4;
    --band-gold-top: #6a5a2a;
    --band-gold-mid: #b59a4a;
    --band-gold-low: #8a7436;
    --band-mint-top: #b9d2b9;
    --band-mint-low: #8fb2a4;
    --band-brown-top: #4a3a2a;
    --band-brown-low: #7a4a22;
    --photo-dark: #1d1a14;
  }
  * { box-sizing: border-box; margin: 0; padding: 0; }
  html, body { width: 1188px; height: 1200px; overflow: hidden; background: var(--page-bg); }
  .canvas { position: relative; width: 1188px; height: 1200px; }
  .cover {
    position: absolute; left: 214px; top: 30px; width: 760px; height: 1140px;
    overflow: hidden; background: var(--photo-dark);
    box-shadow: 0 18px 40px rgba(0,0,0,.25);
  }
  .portraits { position: absolute; left: 0; top: 0; width: 760px; height: 360px; display: flex; }
  .portrait { flex: 1; height: 100%; }
  .portrait--rose { background: radial-gradient(ellipse at 55% 40%, #c9a456 0%, #5d4a24 45%, #1f1a12 85%); }
  .portrait--light { background: radial-gradient(ellipse at 50% 45%, #efd8a0 0%, #a99a62 45%, #3f4a34 90%); }
  .portrait--red { background: radial-gradient(ellipse at 45% 55%, #9a1a1a 0%, #5a1412 40%, #1a1614 85%); }
  .band { position: absolute; left: 0; width: 760px; }
  .band--gold { top: 340px; height: 340px;
    background: linear-gradient(180deg, var(--band-gold-top), var(--band-gold-mid) 45%, var(--band-gold-low)); }
  .band--mint { top: 665px; height: 255px;
    background: linear-gradient(180deg, var(--band-mint-top), var(--band-mint-low)); }
  .band--brown { top: 905px; height: 235px;
    background: linear-gradient(180deg, var(--band-brown-top), var(--band-brown-low) 60%, #3a2a1e); }
  .tear { position: absolute; left: 0; width: 760px; height: 26px; }
  .title-main {
    position: absolute; left: 0; top: 380px; width: 760px; text-align: center;
    font-family: "Anton", "Oswald", sans-serif; font-size: 104px; line-height: 1;
    color: var(--title-red); letter-spacing: 1px;
    text-shadow: 2px 3px 4px rgba(0,0,0,.45);
  }
  .title-sub {
    position: absolute; left: 0; top: 520px; width: 760px; text-align: center;
    font-family: "Oswald", sans-serif; font-weight: 700; font-size: 58px; line-height: 1;
    color: var(--text-white); text-shadow: 2px 3px 4px rgba(0,0,0,.55);
  }
  .title-place {
    position: absolute; left: 0; top: 720px; width: 760px; text-align: center;
    font-family: "Oswald", sans-serif; font-weight: 200; font-size: 118px; line-height: 1;
    color: var(--text-white); letter-spacing: 2px;
    text-shadow: 1px 2px 3px rgba(0,0,0,.45);
  }
  .author {
    position: absolute; left: 0; top: 1000px; width: 760px; text-align: center;
    font-family: "Oswald", sans-serif; font-weight: 200; font-size: 66px; line-height: 1;
    color: var(--text-white); letter-spacing: 1px;
  }
</style>
</head>
<body>
<div class="canvas">
  <div class="cover">
    <div class="portraits">
      <div class="portrait portrait--rose" role="img" aria-label="Photo of a blonde woman in black smelling a red rose"></div>
      <div class="portrait portrait--light" role="img" aria-label="Photo of a fair-haired woman with hands in her hair"></div>
      <div class="portrait portrait--red" role="img" aria-label="Photo of a dark-haired woman in a red dress"></div>
    </div>

    <div class="band band--gold"></div>
    <div class="band band--mint"></div>
    <div class="band band--brown"></div>

    <svg class="tear" style="top:330px" viewBox="0 0 760 26" preserveAspectRatio="none" aria-hidden="true">
      <path fill="var(--paper-edge)" d="M0 8 L40 12 L85 6 L130 13 L180 8 L230 14 L280 9 L330 15 L380 10 L430 16 L480 11 L530 17 L580 12 L630 18 L680 13 L730 19 L760 14 L760 22 L700 20 L640 24 L580 19 L520 23 L460 18 L400 22 L340 17 L280 21 L220 16 L160 20 L100 15 L50 19 L0 16 Z"/>
    </svg>
    <svg class="tear" style="top:655px" viewBox="0 0 760 26" preserveAspectRatio="none" aria-hidden="true">
      <path fill="var(--paper-edge)" d="M0 6 L50 10 L100 5 L150 11 L200 7 L260 13 L320 8 L380 14 L440 9 L500 15 L560 10 L620 16 L690 11 L760 17 L760 24 L690 19 L620 23 L560 18 L500 22 L440 17 L380 21 L320 16 L260 20 L200 15 L140 19 L80 14 L0 18 Z"/>
    </svg>
    <svg class="tear" style="top:895px" viewBox="0 0 760 26" preserveAspectRatio="none" aria-hidden="true">
      <path fill="var(--paper-edge)" d="M0 4 L60 9 L120 5 L180 10 L240 6 L300 12 L360 8 L420 13 L480 9 L540 15 L600 10 L660 16 L720 12 L760 17 L760 23 L700 19 L640 22 L580 17 L520 21 L460 16 L400 20 L340 15 L280 19 L220 14 L160 18 L100 13 L40 17 L0 12 Z"/>
    </svg>

    <h1 class="title-main">TIDLIGERE BRUDE</h1>
    <p class="title-sub">FRA SOLEN, STORMEN</p>
    <p class="title-place">OG LINDEVANG</p>
    <p class="author">JONAS BELTOFT</p>
  </div>
</div>
</body>
</html>
```